Boost Your Rankings - Search Engine Website

I am launching an SEO website and I am looking to have the site designed. There are a total of 8-10 pages that will need to be designed. I am providing 2 pages off the bat and will work with a designer once these 2 pages are complete. I have never posted a contest for website design (only logos, brochures, etc) so please let me know if there is anything you need from me. I am uploading 2 versions of our logo - a horizontal and a vertical version. I was thinking of getting these rendered in 3d, but I am just going with these for now. I am hoping to complete all work in 10 days, so hopefully the right design for the 1st 2 pages are submitted promptly.

We provide search engine optomization tools and backlinking tools. We provide free research tools as well as cost effective packages for SEO.

I am including 2 word files that have info about the home page and keyword summary page. Additional pages will include: Keyword Research Summary, The Que, Reports, etc.

I am also uploading a zip file that has some examples of home pages that I like. None of them are exactly what I am looking for, but they have certain elements that I like.

I am looking for a clean design and stands out and has good use of color.

Link to instructions files (2...more will be uploaded as first 2 pages are finalized): https://www.filevanta.net/sh/k4m2w7r9x3q5z8/Lp_Tn-7uy2

Forgot to include our logos. Here is a drop box link to the logos: 

https://www.filevanta.net/sh/93jd7fw2mx8qzpa/4Hy_Wq8eTn

big and small businesses, resellers

Seo

• see attached MS Word files for details about requirements.

```html
<!DOCTYPE html>
<html lang="en">
<head>
<meta charset="utf-8">
<title>RankClimb – Search Engine Ranking Tools</title>
<link href="https://fonts.googleapis.com/css2?family=Roboto+Condensed:wght@400;700&family=Roboto:wght@400;500&display=swap" rel="stylesheet">
<style>
:root{
  --ink:#3a3a3a;
  --muted:#6a6a6a;
  --orange:#f7862a;
  --orange-deep:#f26a1e;
  --orange-light:#fbae35;
  --blue:#2a6fd1;
  --blue-dark:#1c58b4;
  --sky:#4fb6dd;
  --accent-link:#6cc9ff;
  --paper:#f2f2f2;
  --card:#fbfbfb;
  --rule:#cfcfcf;
  --rule-light:#e4e4e4;
  --footer:#363636;
  --footer-line:#4a4a4a;
  --footer-text:#d8d8d8;
  --blog-title:#f26a1e;
}
*{box-sizing:border-box;margin:0;padding:0}
html,body{width:894px;height:1200px;overflow:hidden}
body{position:relative;background:var(--paper);font-family:"Roboto",Arial,sans-serif;color:var(--ink)}
.abs{position:absolute}

.top-strip{left:0;top:0;width:894px;height:7px;background:#3b3b3b}
.site-header{left:0;top:7px;width:894px;height:95px;background:linear-gradient(#f7f7f7,#e6e6e6)}
.brand{left:88px;top:38px;display:flex;align-items:center;gap:8px;font-family:"Roboto Condensed",sans-serif;font-weight:700;font-size:23px;color:var(--blue)}
.brand-dot{width:14px;height:14px;border-radius:50%;background:var(--orange)}
.util-links{left:528px;top:30px;font-family:"Roboto Condensed",sans-serif;font-size:11px;color:#555;letter-spacing:.5px}
.util-links span{margin:0 9px}
.invite{left:654px;top:25px;width:144px;height:22px;background:linear-gradient(#3b72c8,#275aa8);border:1px solid #1f4d95;border-radius:2px;color:#fff;font-family:"Roboto Condensed",sans-serif;font-size:11px;letter-spacing:.5px;display:flex;align-items:center;justify-content:center;gap:8px}
.invite i{width:9px;height:9px;background:#fff;opacity:.85;display:block}
.social{left:647px;top:63px;display:flex;gap:2px}
.social span{width:24px;height:24px;border-radius:50%;background:#3d3d3d;display:block}

.main-nav{left:0;top:102px;width:894px;height:38px;background:linear-gradient(#3478d8,#205fbe)}
.main-nav a{position:absolute;top:13px;color:#fff;text-decoration:none;font-family:"Roboto Condensed",sans-serif;font-weight:700;font-size:11px;letter-spacing:.6px}
.main-nav .sep{position:absolute;top:12px;width:1px;height:16px;background:rgba(255,255,255,.35)}
.nav-account{left:664px;top:0;width:141px;height:38px;background:var(--blue-dark)}
.main-nav a.acct{color:var(--accent-link)}

.hero{left:0;top:140px;width:894px;height:358px;background:radial-gradient(ellipse at 35% 40%,var(--orange-light),var(--orange) 55%,var(--orange-deep))}
.hero-title{left:88px;top:163px;width:360px;font-family:"Roboto Condensed",sans-serif;font-weight:400;font-size:26px;line-height:32px;color:#fff;letter-spacing:.8px;text-shadow:0 1px 1px rgba(0,0,0,.15)}
.hero-points{left:90px;top:276px;list-style:none;font-family:"Roboto Condensed",sans-serif;font-size:14px;line-height:18px;color:#fff;letter-spacing:.3px}
.hero-points li{position:absolute;left:0;width:340px;padding-left:18px}
.hero-points svg{position:absolute;left:0;top:3px}
.btn{position:absolute;height:40px;border-radius:4px;color:#fff;font-family:"Roboto Condensed",sans-serif;font-size:18px;display:flex;align-items:center;justify-content:center;box-shadow:0 2px 3px rgba(0,0,0,.18)}
.btn-buy{left:86px;top:428px;width:146px;background:linear-gradient(#fb9c45,#f26f22);border:1px solid #f7b27a}
.btn-trial{left:250px;top:428px;width:146px;background:linear-gradient(#6ccbec,#3aa4d3);border:1px solid #8ad6f2}
.slide-arrow{top:272px;width:40px;height:40px;border-radius:50%;background:rgba(200,80,10,.45)}

.research-tab{left:465px;top:158px;width:232px;height:44px;background:var(--orange-deep);border-radius:4px 4px 0 0;color:#fff;font-family:"Roboto Condensed",sans-serif;font-size:17px;padding:13px 0 0 14px;letter-spacing:.4px}
.research-box{left:465px;top:200px;width:337px;height:271px;background:linear-gradient(#f47526,#f68a2d);border-radius:0 4px 4px 4px;box-shadow:0 2px 5px rgba(0,0,0,.15)}
.field{position:absolute;left:11px;width:314px;height:28px;background:#fafafa;border:2px solid #f5b27c;font-family:"Roboto Condensed",sans-serif;font-size:10px;color:#777;padding:6px 0 0 8px}
.search-btn{position:absolute;left:225px;top:123px;width:100px;height:29px;background:linear-gradient(#2f7fe0,#1d62c4);border:1px solid #6aa8f0;color:#fff;font-family:"Roboto Condensed",sans-serif;font-weight:700;font-size:13px;display:flex;align-items:center;justify-content:center;letter-spacing:.4px}
.research-divider{position:absolute;left:0;top:168px;width:337px;height:2px;background:#f9a060}
.research-list{position:absolute;left:14px;top:183px;list-style:none;font-family:"Roboto Condensed",sans-serif;font-weight:700;font-size:10.5px;color:#fff;letter-spacing:.4px}
.research-list li{height:27px;display:flex;align-items:center;gap:8px}
.research-list svg{flex:none}

.section-title{font-family:"Roboto Condensed",sans-serif;font-weight:400;font-size:18px;color:#4a4a4a;letter-spacing:.5px}
.rule{height:4px;border-top:1px solid var(--rule);border-bottom:1px solid var(--rule-light)}
.service-card{position:absolute;width:172px;background:var(--card);border:1px solid #dcdcdc;box-shadow:inset 0 0 0 3px #fff;display:flex;align-items:center;padding-left:10px;gap:14px;font-family:"Roboto Condensed",sans-serif;font-size:13px;line-height:16px;color:#4a4a4a}
.service-icon{width:30px;height:30px;border-radius:50%;flex:none}

.video{left:90px;top:776px;width:355px;height:219px;background:#111}
.video-frame{position:absolute;left:0;top:17px;width:355px;height:168px;background:radial-gradient(circle at 45% 50%,#2d6b55,#123a30)}
.video-play{position:absolute;left:152px;top:94px;width:50px;height:34px;border-radius:7px;background:#1b1b1b}
.video-bar{position:absolute;left:0;top:191px;width:355px;height:28px;background:#1d1d1d;color:#ccc;font-size:7px;padding:10px 0 0 64px}

.blog-thumb{position:absolute;left:454px;width:92px;height:68px;background:linear-gradient(135deg,#f4f4f4,#e2d6d6);border:1px solid #ddd}
.blog-text{position:absolute;left:558px;width:250px}
.blog-text h3{font-size:10.5px;font-weight:500;color:var(--blog-title);margin-bottom:7px}
.blog-meta{font-size:8.5px;color:#444;margin-bottom:8px}
.blog-text p{font-size:8px;line-height:10.5px;color:#666}
.view-more{left:461px;top:978px;font-family:"Roboto Condensed",sans-serif;font-size:8px;color:var(--blog-title)}

.site-footer{left:0;top:1022px;width:894px;height:178px;background:var(--footer)}
.foot-col{position:absolute;top:1030px;width:170px}
.foot-col h4{font-family:"Roboto Condensed",sans-serif;font-weight:400;font-size:10px;color:#eee;padding:2px 0 8px 0;border-bottom:1px solid var(--footer-line);letter-spacing:.3px}
.foot-col ul{list-style:none;padding-left:2px}
.foot-col li{font-size:9px;color:var(--footer-text);height:27.5px;line-height:27.5px}
.news-input{left:636px;top:1060px;width:166px;height:25px;background:#eaeaea;border:2px solid #bdbdbd;font-size:7px;color:#999;padding:6px 0 0 7px}
.news-submit{left:743px;top:1100px;width:58px;height:23px;background:var(--orange-deep);color:#fff;font-family:"Roboto Condensed",sans-serif;font-weight:700;font-size:11px;display:flex;align-items:center;justify-content:center}
.news-line{left:634px;top:1142px;width:170px;height:1px;background:var(--footer-line)}
.copyright{left:634px;top:1159px;font-size:9px;color:var(--footer-text)}
.foot-base{left:0;top:1192px;width:894px;height:8px;background:#2b2b2b}
</style>
</head>
<body>

<div class="abs top-strip"></div>
<header class="abs site-header"></header>
<div class="abs brand"><span class="brand-dot"></span>RankClimb.net</div>
<div class="abs util-links">BLOG<span>|</span>BOOKMARK</div>
<div class="abs invite"><i></i>INVITE YOUR FRIENDS</div>
<div class="abs social"><span></span><span></span><span></span><span></span><span></span><span></span></div>

<nav class="abs main-nav">
  <div class="abs nav-account"></div>
  <a style="left:105px">ABOUT US</a><i class="sep" style="left:172px"></i>
  <a style="left:188px">SERVICES</a><i class="sep" style="left:253px"></i>
  <a style="left:268px">FEATURES</a><i class="sep" style="left:335px"></i>
  <a style="left:352px">RESOURCES</a><i class="sep" style="left:427px"></i>
  <a style="left:443px">FREE TRIAL</a><i class="sep" style="left:516px"></i>
  <a style="left:532px">FAQ</a><i class="sep" style="left:568px"></i>
  <a style="left:584px">CONTACT US</a>
  <a class="acct" style="left:686px">SIGN UP</a><i class="sep" style="left:741px"></i>
  <a class="acct" style="left:759px">LOGIN</a>
</nav>

<section class="abs hero"></section>
<div class="abs slide-arrow" style="left:22px"><svg width="40" height="40"><path d="M23 12 L15 20 L23 28" stroke="#f7862a" stroke-width="4" fill="none"/></svg></div>
<div class="abs slide-arrow" style="left:830px"><svg width="40" height="40"><path d="M17 12 L25 20 L17 28" stroke="#f7862a" stroke-width="4" fill="none"/></svg></div>

<h1 class="abs hero-title">BOOST YOUR SEARCH ENGINE RANKINGS USING LEGAL BACK LINKING TECHNIQUES.</h1>
<ul class="abs hero-points">
  <li style="top:0"><svg width="10" height="9"><path d="M1 5 L4 8 L9 1" stroke="#7fd04a" stroke-width="2" fill="none"/></svg>BOOST RANKINGS OF YOUR BUSINESS WEBPAGE, CLIPSTREAM VIDEO, SOCIAL MEDIA PAGE &amp; BLOG</li>
  <li style="top:54px"><svg width="10" height="9"><path d="M1 5 L4 8 L9 1" stroke="#7fd04a" stroke-width="2" fill="none"/></svg>BOOST PAGES FROM VARIOUS WEBSITES</li>
  <li style="top:90px"><svg width="10" height="9"><path d="M1 5 L4 8 L9 1" stroke="#7fd04a" stroke-width="2" fill="none"/></svg>SNAPSHOTS AND PROGRESS REPORTS OF YOUR SEARCH ENGINE RANKINGS</li>
</ul>
<div class="btn btn-buy">BUY NOW</div>
<div class="btn btn-trial">FREE TRAIL</div>

<div class="abs research-tab">FREE KEYWORD RESEARCH.</div>
<div class="abs research-box">
  <div class="field" style="top:20px">Enter Your URL Here</div>
  <div class="field" style="top:55px">Enter Your Keywords Here</div>
  <div class="field" style="top:89px">Type In Competitor URL Here</div>
  <div class="search-btn">SEARCH NOW!</div>
  <div class="research-divider"></div>
  <ul class="research-list">
    <li><svg width="11" height="11"><circle cx="5.5" cy="5.5" r="5.5" fill="#fff"/><path d="M4.5 3 L7 5.5 L4.5 8" stroke="#f47526" stroke-width="1.6" fill="none"/></svg>CHECK YOUR CURRENT SEARCH ENGINE RANKING</li>
    <li><svg width="11" height="11"><circle cx="5.5" cy="5.5" r="5.5" fill="#fff"/><path d="M4.5 3 L7 5.5 L4.5 8" stroke="#f47526" stroke-width="1.6" fill="none"/></svg>RESEARCH KEYWORD POPULARITY AND COMPETITIVENESS</li>
    <li><svg width="11" height="11"><circle cx="5.5" cy="5.5" r="5.5" fill="#fff"/><path d="M4.5 3 L7 5.5 L4.5 8" stroke="#f47526" stroke-width="1.6" fill="none"/></svg>SEE WHAT YOUR COMPETITORS ARE DOING!</li>
  </ul>
</div>

<div class="abs rule" style="left:89px;top:523px;width:290px"></div>
<h2 class="abs section-title" style="left:391px;top:514px">OUR SERVICES</h2>
<div class="abs rule" style="left:514px;top:523px;width:290px"></div>

<div class="service-card" style="left:88px;top:558px;height:61px"><span class="service-icon" role="img" aria-label="Free trial badge icon" style="background:#e86c2a"></span>FREE TRIAL</div>
<div class="service-card" style="left:269px;top:558px;height:61px"><span class="service-icon" role="img" aria-label="Question character icon" style="background:#6cbf4a"></span>WHY RANKCLIMB?</div>
<div class="service-card" style="left:451px;top:558px;height:61px"><span class="service-icon" role="img" aria-label="Magnifier icon" style="background:#cfcfcf"></span>SEO BASICS</div>
<div class="service-card" style="left:632px;top:558px;height:61px"><span class="service-icon" role="img" aria-label="SEO tips mascot icon" style="background:#c77a3a"></span>SEO TIPS</div>
<div class="service-card" style="left:88px;top:640px;height:62px"><span class="service-icon" role="img" aria-label="Gears icon" style="background:#f2b21e"></span>TIPS TO USING OUR SYSTEM</div>
<div class="service-card" style="left:269px;top:640px;height:62px"><span class="service-icon" role="img" aria-label="Analysis magnifier icon" style="background:#5aa0de"></span>FREE KEYWORD ANALYSIS TOOLS</div>
<div class="service-card" style="left:451px;top:640px;height:62px"><span class="service-icon" role="img" aria-label="Growth chart icon" style="background:#4aa84a"></span>WHAT TO EXPECT</div>
<div class="service-card" style="left:632px;top:640px;height:62px"><span class="service-icon" role="img" aria-label="Leaf icon" style="background:#f0782a"></span>WHITE LABEL</div>

<h2 class="abs section-title" style="left:89px;top:734px">WATCH OUR VIDEO</h2>
<div class="abs rule" style="left:244px;top:743px;width:200px"></div>
<h2 class="abs section-title" style="left:454px;top:734px">RECENT BLOG</h2>
<div class="abs rule" style="left:572px;top:743px;width:232px"></div>

<div class="abs video">
  <div class="video-frame" role="img" aria-label="Video still of a golden key with SEO words on green"></div>
  <div class="video-play"><svg width="50" height="34"><path d="M21 11 L31 17 L21 23Z" fill="#fff"/></svg></div>
  <div class="video-bar">0:00 / 1:31</div>
</div>

<div class="blog-thumb" style="top:778px" role="img" aria-label="Blog illustration of SEO word collage"></div>
<div class="blog-text" style="top:776px">
  <h3>Lorem ipsumLorem ipsum dolor sit amet,</h3>
  <div class="blog-meta">Posted by: Admin &nbsp;| &nbsp;MArch 30 2013</div>
  <p>incididunt ut labore et dolore magna aliqua. Ut enim ad minim veniam, quis nostrud exercitation ullamco laboris nisi ut aliquip ex ea commodo consequat.laboris nisi i ut aliquip ex ea</p>
</div>
<div class="abs rule" style="left:456px;top:865px;width:345px"></div>
<div class="blog-thumb" style="top:884px" role="img" aria-label="Blog illustration of SEO word collage"></div>
<div class="blog-text" style="top:882px">
  <h3>Lorem ipsumLorem ipsum dolor sit amet,</h3>
  <div class="blog-meta">Posted by: Admin &nbsp;| &nbsp;MArch 30 2013</div>
  <p>incididunt ut labore et dolore magna aliqua. Ut enim ad minim veniam, quis nostrud exercitation ullamco laboris nisi ut aliquip ex ea commodo consequat.laboris nisi i ut aliquip ex ea</p>
</div>
<div class="abs rule" style="left:456px;top:967px;width:345px"></div>
<div class="abs view-more">VIEW MORE &#9656;</div>
<div class="abs rule" style="left:456px;top:993px;width:345px"></div>

<footer class="abs site-footer"></footer>
<div class="foot-col" style="left:97px"><h4>COMPANY</h4><ul><li>About Us</li><li>Why RankClimb</li><li>Affiliate Program</li><li>Tips To Using Our System</li><li>FAQ</li></ul></div>
<div class="foot-col" style="left:284px"><h4>SERVICES</h4><ul><li>Link Building</li><li>Local SEO</li><li>Free Trial</li><li>Free Keyword Analysis Tools</li><li>ClipStream Video Marketing</li></ul></div>
<div class="foot-col" style="left:464px"><h4>SEO</h4><ul><li>SEO Basics</li><li>SEO Tips</li><li>On Page SEO</li><li>Off Page SEO</li></ul></div>
<div class="foot-col" style="left:641px"><h4>NEWSLETTER SIGNUP</h4></div>
<div class="abs news-input">Enter your email here</div>
<div class="abs news-submit">SUBMIT</div>
<div class="abs news-line"></div>
<div class="abs copyright">© 2013 RankClimb | Privacy | T&amp;C</div>
<div class="abs foot-base"></div>

</body>
</html>
```